Harborstone Lending Business Card Design

We are looking for a nice looking business card design. I'd prefer something other than white for the background but white is ok if necessary. I'm uploading two versions of my picture, one is square and one is rounded. Also a couple of versions of the logo for white backgrounds as well as one for darker backgrounds.

Target Market(s)

Realtors and prospective clients

Industry/Entity Type

Mortgage

Contact Information for Business Card

Double sided business card. Not sure what is needed here.

Colors

Designer to choose colors to be used in the design.

Requirements
Must have
• Name: Marcus Pellham
• Title: Senior Mortgage Advisor
• Email: marcuspellham@harborstonelending.example
• website: www.marcuspellhamhomeloangroup.example
• Address: 4670 W 2850 N, STE 215 Salt Lake City, UT 84192
• Phone: 801-555-0187
• nmls# 948217
• Logo is on our webstie. www.harborstonelending.example
• Picture
Nice to have
• Colors could be similar to our website www.harborstonelending.example
• A list of what we do (VA Loans, FHA Loans, Conventional Loans, USDA Loans)

```html
<!DOCTYPE html>
<html lang="en">
<head>
<meta charset="utf-8">
<title>Harborstone Lending Business Card</title>
<link rel="stylesheet" href="https://fonts.googleapis.com/css2?family=Roboto:wght@400;500;700&family=Roboto+Condensed:wght@700&display=swap">
<style>
  :root {
    --page-bg: #ece8e2;
    --card-dark: #1a1b1d;
    --card-light: #f4f4f4;
    --ink: #111111;
    --ink-soft: #3c3c3c;
    --title-grey: #a5a5a5;
    --rule: #7a7a7a;
    --white: #ffffff;
  }
  * { margin: 0; padding: 0; box-sizing: border-box; }
  html, body {
    width: 1200px; height: 960px; overflow: hidden;
    background: var(--page-bg);
    font-family: "Roboto", Arial, sans-serif;
  }
  .canvas { position: relative; width: 1200px; height: 960px; }
  .card {
    position: absolute; left: 320px; width: 600px;
    border-radius: 16px;
  }
  .card--front { top: 105px; height: 345px; background: var(--card-dark); color: var(--white); }
  .card--back { top: 493px; height: 335px; background: var(--card-light); color: var(--ink); }

  .brand {
    position: absolute; display: flex; align-items: center; gap: 12px;
    font-weight: 700; letter-spacing: 3px; text-transform: uppercase; white-space: nowrap;
  }
  .brand__mark { width: 14px; height: 14px; border-radius: 50%; background: currentColor; flex: none; }
  .card--front .brand { left: 0; right: 0; justify-content: center; top: 150px; font-size: 32px; color: var(--white); }
  .card--back .brand { right: 32px; top: 58px; font-size: 25px; color: var(--ink); }

  .services {
    position: absolute; left: 0; right: 0; top: 291px;
    text-align: center; font-size: 14px; color: var(--white);
  }
  .services__sep { font-size: 10px; margin: 0 3px; position: relative; top: -1px; }

  .person { position: absolute; left: 24px; top: 187px; }
  .person__name { font-family: "Roboto Condensed", "Arial Narrow", sans-serif; font-weight: 700; font-size: 20px; letter-spacing: 0.3px; }
  .person__title { font-size: 14.5px; color: var(--title-grey); letter-spacing: 0.2px; margin-top: 1px; }
  .divider { position: absolute; left: 24px; right: 32px; top: 238px; height: 1px; background: var(--rule); }

  .contact-list { position: absolute; left: 24px; top: 250px; list-style: none; font-size: 14px; color: var(--ink-soft); }
  .contact-list li { display: flex; align-items: center; gap: 9px; height: 19.5px; }
  .contact-list svg { width: 12px; height: 12px; fill: var(--ink); flex: none; }

  .address { position: absolute; right: 30px; top: 251px; text-align: right; font-size: 14px; line-height: 19px; color: var(--ink-soft); }
</style>
</head>
<body>
<main class="canvas">
  <section class="card card--front" aria-label="Card front">
    <div class="brand"><span class="brand__mark"></span>Harborstone Lending</div>
    <p class="services">VA Loans <span class="services__sep">★</span>FHA Loans <span class="services__sep">★</span>Conventional Loans <span class="services__sep">★</span>USDA Loans</p>
  </section>

  <section class="card card--back" aria-label="Card back">
    <div class="brand"><span class="brand__mark"></span>Harborstone Lending</div>
    <div class="person">
      <h1 class="person__name">MARCUS PELLHAM</h1>
      <p class="person__title">SENIOR MORTGAGE ADVISOR</p>
    </div>
    <div class="divider"></div>
    <ul class="contact-list">
      <li><svg viewBox="0 0 24 24"><path d="M6.6 10.8a15.1 15.1 0 0 0 6.6 6.6l2.2-2.2c.3-.3.7-.4 1-.2 1.1.4 2.3.6 3.6.6.6 0 1 .4 1 1V20c0 .6-.4 1-1 1A17 17 0 0 1 3 4c0-.6.4-1 1-1h3.5c.6 0 1 .4 1 1 0 1.3.2 2.5.6 3.6.1.3 0 .7-.2 1z"/></svg>801-555-0187</li>
      <li><svg viewBox="0 0 24 24"><path d="M2 5h20v14H2zm2 2v.5l8 5 8-5V7zm0 2.8V17h16V9.8l-8 5z"/></svg>marcuspellham@harborstonelending.example</li>
      <li><svg viewBox="0 0 24 24"><path d="M12 2a10 10 0 1 0 0 20 10 10 0 0 0 0-20zm-1 17.9A8 8 0 0 1 4.1 10.6L9 15.5v1a2 2 0 0 0 2 2zm6.9-2.5A2 2 0 0 0 16 16h-1v-3a1 1 0 0 0-1-1H8v-2h2a1 1 0 0 0 1-1V7h2a2 2 0 0 0 2-2v-.4a8 8 0 0 1 2.9 12.8z"/></svg>marcuspellhamhomeloangroup.example</li>
    </ul>
    <address class="address" style="font-style:normal">
      4670 W 2850 N, STE 215<br>
      Salt Lake City, UT 84192<br>
      nmls# 948217
    </address>
  </section>
</main>
</body>
</html>
```